Sign Up Page Design

We wish to revamp the sign up page of our real estate website (www.quillbrookvantagepoint.com) in order to improve conversion rate. This sign up page has two steps, thus you should come up with 2 pages of sample. We are more interested in getting a design created by a UX designer who has already created other sign up pages and knows the mind of an online buyer. We are sending attached the screenshot of the current sign up page for you to take as basis. Feel free to improve them and come up with something better which can help increase conversion rate.
Updates

We have changed the project settings to NON REFUNDABLE.... so please keep sending your designs. We look forward for your creativity!!!

Industry/Entity Type

Real Estate

```html
<!DOCTYPE html>
<html lang="en">
<head>
<meta charset="utf-8">
<title>Choose Your Plan – Quillbrook Vantage Point</title>
<link href="https://fonts.googleapis.com/css2?family=Open+Sans:ital,wght@0,400;0,600;0,700;1,400&family=Archivo+Black&display=swap" rel="stylesheet">
<style>
:root{
  --blue:#1f6fa8;
  --blue-dark:#17568a;
  --green:#6ca935;
  --orange:#f57f0a;
  --orange-light:#ff8a00;
  --text:#444;
  --muted:#666;
  --bg:#efefef;
  --footer:#555;
  --small:Arial,Helvetica,sans-serif;
}
*{box-sizing:border-box;margin:0;padding:0}
html,body{width:1200px;height:1200px;overflow:hidden}
body{position:relative;background:var(--bg);font-family:"Open Sans",Arial,sans-serif;color:var(--text)}
.abs{position:absolute}
.brand{left:104px;top:14px;display:flex;align-items:center;gap:8px}
.brand-mark{width:36px;height:36px;background:var(--blue);border-radius:4px}
.brand-name{font-size:20px;font-weight:600;color:var(--blue)}
.main-card{left:100px;top:80px;width:1000px;height:876px;background:#fff;box-shadow:0 1px 3px rgba(0,0,0,.15)}
.side-rule{left:806px;top:98px;height:795px;border-left:1px dotted #ccc}
.headline-mark{left:188px;top:122px;width:46px;height:52px;border-radius:40% 10% 40% 10%;background:linear-gradient(135deg,#ffa040,#f57f0a)}
.headline{left:229px;top:103px;font-size:27px;font-weight:400;color:var(--blue);letter-spacing:.5px;white-space:nowrap}
.headline em{color:var(--green);font-weight:700}
.plan{background:#fff;border:1px solid #d8d8d8;border-radius:8px;box-shadow:0 1px 4px rgba(0,0,0,.12);overflow:hidden}
.plan-head{background:#f2f2f2;text-align:center}
.plan-title{font-family:"Archivo Black",Arial,sans-serif;font-size:24px;color:#333;letter-spacing:1px}
.plan-price{font-size:19px;color:var(--muted)}
.plan-btn{position:absolute;left:0;right:0;bottom:0;color:#fff;font-weight:700;font-size:15px;display:flex;align-items:center;justify-content:center;gap:8px}
.radio{width:11px;height:11px;border-radius:50%;background:#fff;border:2px solid #ccc;flex:none}
.radio.on{background:var(--blue);box-shadow:inset 0 0 0 2px #fff}
.monthly{left:121px;top:196px;width:207px;height:288px}
.monthly .plan-head{height:84px;padding-top:14px}
.monthly .plan-btn{height:44px;background:linear-gradient(#f57f0a,#e86a00)}
.feature{display:flex;gap:8px;padding:14px 12px;font-family:var(--small);font-size:12px;line-height:18px;color:#555}
.trial{left:342px;top:170px;width:232px;height:339px}
.trial .plan-head{height:82px;padding-top:12px}
.trial .plan-sub{font-size:19px;color:var(--muted)}
.trial-offer{text-align:center;margin-top:60px;font-family:var(--small);font-weight:700;font-size:21px;color:#777;line-height:26px}
.trial-offer .now{color:var(--orange)}
.trial .plan-btn{height:52px;background:linear-gradient(#4f8f1e 0,#7fbd3c 30%,#8cc63f)}
.annual{left:586px;top:196px;width:207px;height:288px}
.annual .plan-head{height:84px;padding-top:14px}
.annual-row{font-family:var(--small);font-size:12px;color:#555;padding:14px 12px 12px}
.annual-row.alt{background:#f2f2f2;height:48px}
.annual .plan-btn{height:44px;background:linear-gradient(#2a86c8,#1c6aa8)}
.pay-title{left:100px;width:712px;top:556px;text-align:center;font-size:20px;font-weight:400;color:#444;letter-spacing:.5px}
.pay-opt{top:600px;width:173px;height:54px;border:1px solid #ddd;border-radius:8px;background:linear-gradient(#fff,#f3f3f3);display:flex;align-items:center;gap:6px;padding-left:12px;font-size:16px;color:#444}
.pay-icon{width:38px;height:32px;border-radius:3px;margin-left:auto;margin-right:10px}
.btn{top:680px;height:43px;border-radius:6px;color:#fff;font-weight:700;font-size:20px;display:flex;align-items:center;padding-left:10px;gap:10px;box-shadow:0 1px 2px rgba(0,0,0,.3)}
.btn-back{left:255px;width:111px;background:linear-gradient(#2a86c8,#155f99)}
.btn-go{left:386px;width:266px;background:linear-gradient(#ff8f1a,#e06a00);padding-left:12px;gap:8px}
.btn-circle{width:18px;height:18px;border-radius:50%;background:#fff;display:flex;align-items:center;justify-content:center}
.rule{left:115px;top:751px;width:670px;border-top:1px dotted #ccc}
.badge{border-radius:6px}
.secure{left:564px;top:794px;font-family:var(--small);font-size:12.5px;line-height:18px;color:#444}
.note{left:140px;top:871px;width:610px;font-family:var(--small);font-size:10.5px;line-height:18px;color:#555}
.bubble{left:825px;width:263px;height:138px;border-radius:22px;color:#fff;font-style:italic;font-size:11px;line-height:18px;padding:31px 22px 0 24px;text-align:justify}
.bubble.green{top:100px;background:var(--green)}
.bubble.orange{top:320px;background:var(--orange-light)}
.quote{position:absolute;font-family:Georgia,serif;font-style:normal;font-weight:700;font-size:24px;line-height:1}
.author{left:835px;font-size:10.5px;color:#333}
.side-sep{left:822px;width:266px;border-top:1px dotted #ccc}
.faq{left:820px;top:565px;list-style:none;font-family:var(--small);font-size:12px;color:#444;width:272px}
.faq li{position:relative;padding-left:15px;margin-bottom:16px;line-height:14px}
.faq li::before{content:"";position:absolute;left:0;top:3px;border-left:5px solid var(--orange);border-top:4px solid transparent;border-bottom:4px solid transparent}
.stat{top:981px;height:130px;background:linear-gradient(#fff,#f0f0f0);border:1px solid #ddd;border-radius:8px;text-align:center;box-shadow:0 2px 4px rgba(0,0,0,.1)}
.stat-num{font-family:"Archivo Black",Arial,sans-serif;font-size:35px;margin-top:24px;letter-spacing:1px;line-height:44px}
.stat-label{font-size:15px;color:#333;letter-spacing:.5px;margin-top:14px}
.footer{left:0;top:1144px;width:1200px;height:56px;background:var(--footer);color:#fff;font-family:var(--small);font-size:12px;text-align:center;padding-top:10px;line-height:18px}
</style>
</head>
<body>
<div class="abs brand"><span class="brand-mark"></span><span class="brand-name">Quillbrook Vantage Point</span></div>

<div class="abs main-card"></div>
<div class="abs side-rule"></div>

<div class="abs headline-mark" role="img" aria-label="Decorative orange pointer toward the plans"></div>
<h1 class="abs headline">Choose the plan <em>that's right</em> for you</h1>

<section class="abs plan monthly">
  <div class="plan-head"><div class="plan-title">Monthly</div><div class="plan-price">$39.95/mo</div></div>
  <div class="feature">
    <svg width="20" height="22" viewBox="0 0 20 22" aria-hidden="true"><rect x="1" y="4" width="16" height="16" fill="none" stroke="#6ca935" stroke-width="2"/><path d="M4 11 L9 17 L19 2" fill="none" stroke="#6ca935" stroke-width="3"/></svg>
    <span>Cancle at any time during your monthly subscription</span>
  </div>
  <div class="plan-btn"><span class="radio"></span>I'll go monthly</div>
</section>

<section class="abs plan trial">
  <div class="plan-head"><div class="plan-title">7-Day Trail*</div><div class="plan-sub">Limited time offer</div></div>
  <div class="trial-offer">WAS $9.95 NOW<br><span class="now">$3.95</span><br>ACT NOW!</div>
  <div class="plan-btn"><span class="radio on"></span>I'll try for 7 days</div>
</section>

<section class="abs plan annual">
  <div class="plan-head"><div class="plan-title">Annual</div><div class="plan-price">$99.00</div></div>
  <div class="annual-row">Only $8.25/mo gfor 12 months!</div>
  <div class="annual-row alt">One times fee only-No Rebill</div>
  <div class="plan-btn"><span class="radio"></span>I'll go Annual</div>
</section>

<h2 class="abs pay-title">Chose Your Payment From</h2>
<div class="abs pay-opt" style="left:279px"><span class="radio on"></span>Credit Card<span class="pay-icon" role="img" aria-label="Credit card icon" style="background:linear-gradient(135deg,#f6c23a,#2a86c8)"></span></div>
<div class="abs pay-opt" style="left:463px"><span class="radio"></span>&nbsp;Cheque<span class="pay-icon" role="img" aria-label="Cheque icon" style="background:linear-gradient(#f4d4d4,#e05050)"></span></div>

<div class="abs btn btn-back"><span class="btn-circle"><svg width="8" height="10"><path d="M7 0 L0 5 L7 10Z" fill="#155f99"/></svg></span>Back</div>
<div class="abs btn btn-go">Proceed To Checkout<span class="btn-circle" style="margin-left:6px"><svg width="8" height="10"><path d="M1 0 L8 5 L1 10Z" fill="#e06a00"/></svg></span></div>

<div class="abs rule"></div>
<div class="abs badge" role="img" aria-label="Security certificate badge" style="left:250px;top:782px;width:125px;height:58px;background:#e8e2d6"></div>
<div class="abs badge" role="img" aria-label="Payment processor badge" style="left:403px;top:786px;width:94px;height:54px;background:#dfe6f0"></div>
<svg class="abs" style="left:533px;top:797px" width="24" height="34" viewBox="0 0 24 34" aria-hidden="true"><path d="M5 14 V9 a7 7 0 0 1 14 0 V14" fill="none" stroke="#888" stroke-width="3"/><circle cx="12" cy="23" r="10" fill="#2a6fb0"/><circle cx="12" cy="23" r="3" fill="#fff"/></svg>
<div class="abs secure">Secure Page<br>128-bit Strong Encryption</div>
<p class="abs note">* If you would like to continue receiving our services beyond the 7-day trial period, simply do nothing and you will only be charged $39.95 per month. There is a "Contact" button on top of every page throughout the entire site that will redirect you to an area where you can end your membership - no questions asked.</p>

<blockquote class="abs bubble green"><span class="quote" style="left:10px;top:18px">“</span>Lorem Ipsum is simply dummy text of the printing and typesetting industry. Lorem Ipsum has been the industry's standard dummy text ever since the 1500s,<span class="quote" style="right:38px;bottom:22px">”</span></blockquote>
<svg class="abs" style="left:1008px;top:236px" width="38" height="38" aria-hidden="true"><path d="M2 0 L24 0 L22 14Z" fill="#6ca935"/><circle cx="20" cy="21" r="15" fill="none" stroke="#ddd" stroke-width="2"/><circle cx="20" cy="21" r="9" fill="none" stroke="#ddd" stroke-width="2"/><circle cx="20" cy="21" r="3" fill="#ddd"/></svg>
<div class="abs author" style="top:251px">Martin Helloway, Brookfield, VT</div>
<div class="abs side-sep" style="top:297px"></div>

<blockquote class="abs bubble orange"><span class="quote" style="left:10px;top:18px">“</span>Lorem Ipsum is simply dummy text of the printing and typesetting industry. Lorem Ipsum has been the industry's standard dummy text ever since the 1500s,<span class="quote" style="right:38px;bottom:22px">”</span></blockquote>
<svg class="abs" style="left:1008px;top:456px" width="38" height="38" aria-hidden="true"><path d="M2 0 L24 0 L22 14Z" fill="#ff8a00"/><circle cx="20" cy="21" r="15" fill="none" stroke="#ddd" stroke-width="2"/><circle cx="20" cy="21" r="9" fill="none" stroke="#ddd" stroke-width="2"/><circle cx="20" cy="21" r="3" fill="#ddd"/></svg>
<div class="abs author" style="top:471px">Martin Helloway, Brookfield, VT</div>
<div class="abs side-sep" style="top:528px"></div>

<ul class="abs faq">
  <li>Why do I have to pay for the 7 Day Trail?</li>
  <li>What kind of properties will I find in this Sites?</li>
  <li>Can I really Savv Money when buying a new home?</li>
  <li>How do I contact Coustomer Services?</li>
</ul>

<div class="abs stat" style="left:100px;width:314px"><div class="stat-num" style="color:var(--orange)">Since 1998</div><div class="stat-label">16-year track record of excellence</div></div>
<div class="abs stat" style="left:451px;width:313px"><div class="stat-num" style="color:var(--blue-dark)">2,000,000+</div><div class="stat-label">properties listed on our site</div></div>
<div class="abs stat" style="left:787px;width:313px"><div class="stat-num" style="color:var(--green);margin-top:26px">2,300+</div><div class="stat-label">new members last month</div></div>

<footer class="abs footer">
  www.quillbrookvantagepoint.com, 420 Lantern Cove Rd, 12, Harbor Glen, FL 33099 &nbsp;&nbsp;&nbsp; | &nbsp;&nbsp;&nbsp; FAX: 1-555-014-2288<br>
  Terms and ConditionsPrivacy PolicyCopyright © 1998-2014 QuillbrookVantagePoint.com Inc., All Rights Reserved.
</footer>
</body>
</html>
```